Volterix Power Flyer

Volterix has developed a device that can properly align incoming electrical current into major energy usage facilities like hotels and hospitals. Designed in the UK, it has shown guaranteed energy savings of 7%. Now being introduced into the USA, our focus is on States that have highest energy costs like Hawaii, CA and NY. I am looking for design help with a 8.5X11 flyer that can be customized for each prospective hotel property client. Content will stay the same and once layout chosen, would like to be able to change the Picture of each prospective hotel site on front of flyer. All the info and basics of layout are established. Simply need some professional help to further design and make it print ready. Logo will need to be adjusted but basic design for that is established also.

```html
<!DOCTYPE html>
<html lang="en">
<head>
<meta charset="utf-8">
<title>Volterix Power Flyer</title>
<link href="https://fonts.googleapis.com/css2?family=Poppins:ital,wght@0,400;0,600;0,700;0,800;1,400&display=swap" rel="stylesheet">
<style>
  :root {
    --backdrop: #545655;
    --paper: #ffffff;
    --forest: #2a6e57;
    --lime: #c3d52f;
    --navy: #244a6b;
    --ink: #2f2f2f;
    --logo-ink: #23324a;
    --sky-top: #8fc7ee;
    --sky-low: #cfe6f6;
    --facade: #e9e3da;
    --palm: #4f7f3a;
    --water: #4fb6cf;
  }
  * { margin: 0; padding: 0; box-sizing: border-box; }
  html, body { width: 1200px; height: 1200px; overflow: hidden; }
  body {
    background: var(--backdrop);
    font-family: "Poppins", Arial, sans-serif;
    position: relative;
  }
  .flyer {
    position: absolute;
    left: 255px; top: 153px;
    width: 691px; height: 894px;
    background: var(--paper);
    overflow: hidden;
  }
  .headline {
    position: absolute; left: 0; right: 0; top: 35px;
    text-align: center;
    color: var(--forest);
    font-weight: 800;
    font-size: 26.5px;
    line-height: 28.5px;
    letter-spacing: -0.6px;
    text-transform: uppercase;
  }
  .intro {
    position: absolute; left: 40px; top: 122px; width: 625px;
    font-size: 13.4px; line-height: 19px;
    color: var(--ink);
  }
  .hotel-photo {
    position: absolute; left: 0; top: 196px;
    width: 691px; height: 362px; display: block;
  }
  .savings {
    position: absolute; left: 52px; top: 612px;
  }
  .savings-figure {
    position: absolute; left: 0; top: 0;
    font-weight: 800; font-size: 64px; line-height: 60px;
    color: var(--forest); letter-spacing: -3px;
  }
  .savings-figure .pct { font-weight: 400; font-size: 58px; letter-spacing: 0; }
  .savings-label {
    position: absolute; left: 83px; top: 9px; width: 260px;
    font-weight: 800; font-size: 26px; line-height: 25px;
    color: var(--forest); letter-spacing: -0.4px;
    text-transform: uppercase;
  }
  .savings-note {
    position: absolute; left: 0; top: 57px; white-space: nowrap;
    font-size: 18.5px; color: var(--ink);
  }
  .savings-note strong { font-weight: 700; }
  .footnote {
    position: absolute; left: -3px; top: 86px; white-space: nowrap;
    font-size: 7.6px; font-style: italic; color: var(--ink);
  }
  .benefits {
    position: absolute; left: 417px; top: 584px; width: 260px;
    list-style: none;
  }
  .benefits li {
    position: relative; padding-left: 23px;
    font-size: 15.8px; line-height: 22.6px; color: var(--ink);
    margin-bottom: 2px;
  }
  .benefits li strong { color: var(--navy); font-weight: 700; }
  .benefits .tick {
    position: absolute; left: 0; top: 6px; width: 12px; height: 10px;
  }
  .footer-band {
    position: absolute; left: 0; top: 740px;
    width: 691px; height: 154px; display: block;
  }
  .brand {
    position: absolute; left: 62px; top: 827px;
    display: flex; align-items: center; gap: 12px;
  }
  .brand-mark { width: 30px; height: 30px; background: var(--forest); }
  .brand-name {
    font-weight: 600; font-size: 30px; line-height: 40px;
    color: var(--logo-ink); letter-spacing: 1px;
  }
  .contact {
    position: absolute; left: 418px; top: 819px; width: 220px;
    text-align: center; color: var(--logo-ink);
  }
  .contact-name { font-weight: 700; font-size: 15.5px; line-height: 19px; }
  .contact-email { font-size: 15.5px; line-height: 19px; }
  .contact-phone { font-weight: 700; font-size: 16.5px; line-height: 20px; }
</style>
</head>
<body>
  <main class="flyer">
    <h1 class="headline">Slash your Maui hotel’s<br>energy costs by 7%—guaranteed</h1>

    <p class="intro">In Maui's high-cost, high-use energy environment, Volterix guarantees a 7% reduction in electricity costs for hotels that install our Phase Pro units-and found most properties achieve closer to 10% in real-world conditions.</p>

    <svg class="hotel-photo" viewBox="0 0 691 362" role="img" aria-label="Photo of the prospective hotel: a white multi-storey resort with red tile roofs, palm trees and turquoise water in front">
      <defs>
        <linearGradient id="sceneTone" x1="0" y1="0" x2="0" y2="1">
          <stop offset="0" stop-color="var(--sky-top)"/>
          <stop offset="0.25" stop-color="var(--sky-low)"/>
          <stop offset="0.45" stop-color="var(--facade)"/>
          <stop offset="0.72" stop-color="#b9c3a5"/>
          <stop offset="0.8" stop-color="var(--palm)"/>
          <stop offset="0.86" stop-color="#3d4a3e"/>
          <stop offset="0.9" stop-color="var(--water)"/>
          <stop offset="1" stop-color="#7fd0e0"/>
        </linearGradient>
      </defs>
      <rect width="691" height="362" fill="url(#sceneTone)"/>
      <path d="M0 312 Q345 412 691 303 L691 362 L0 362 Z" fill="var(--paper)"/>
    </svg>

    <section class="savings">
      <div class="savings-figure">7<span class="pct">%</span></div>
      <div class="savings-label">Energy savings guaranteed</div>
      <p class="savings-note">Most properties see closer to <strong>10%</strong>**</p>
      <p class="footnote">*Actual savings depend on your facility’s energy usage patterns.</p>
    </section>

    <ul class="benefits">
      <li><svg class="tick" viewBox="0 0 12 10"><path d="M1 5.5 L4.5 9 L11 1" fill="none" stroke="var(--navy)" stroke-width="1.4"/></svg><strong>7% lower electricity costs</strong>, guaranteed</li>
      <li><svg class="tick" viewBox="0 0 12 10"><path d="M1 5.5 L4.5 9 L11 1" fill="none" stroke="var(--navy)" stroke-width="1.4"/></svg><strong>No upfront</strong> capital investment required</li>
      <li><svg class="tick" viewBox="0 0 12 10"><path d="M1 5.5 L4.5 9 L11 1" fill="none" stroke="var(--navy)" stroke-width="1.4"/></svg><strong>Zero maintenance</strong>, automated solution that starts saving on day one.</li>
    </ul>

    <svg class="footer-band" viewBox="0 0 691 154" aria-hidden="true">
      <path d="M0 0 Q345 78 691 0 L691 154 L0 154 Z" fill="var(--forest)"/>
      <path d="M0 24 Q345 98 691 24 L691 154 L0 154 Z" fill="var(--lime)"/>
    </svg>

    <div class="brand">
      <span class="brand-mark"></span>
      <span class="brand-name">KMR ENERGY</span>
    </div>

    <address class="contact" style="font-style:normal">
      <div class="contact-name">DANIEL KEALOHA</div>
      <div class="contact-email">dk.services808@example.com</div>
      <div class="contact-phone">(808) 555-0147</div>
    </address>
  </main>
</body>
</html>
```